Online Banner and skyscrapper ads

Design ads for real estate company in Australia to be used on Plot fnder.com.au details below
sizes
Leaderboard Specifications
• Dimensions: 728×90px
• Format: HTML5 or Animated/Static Gif
• Max file size: 100kb (HTML5), 80kb (GIF, JPG, PNG)
• Back-up image: 40kb (GIF, JPG, PNG). Back-up image only required if you supply an HTML5 banner.
• Looping: Yes
• See Leaderboard for more information.
Email Alert Strip Ad (EASA) Specifications
• Dimensions: 472×114 px
• Format: JPEG, PNG or Static GIF
• File Size: 20kb
• Looping: No
Skyscraper Specifications
• Dimensions: 160x600px
• Looping: Yes
• See Skyscraper for more information.
Mega Skyscraper Specifications
• Dimensions: 300x600px
• Format: HTML5 or Animated/Static GIF
• File size: 100kb (Html5) or 80kb (GIF, JPG, PNG)
• Back-up image: 40kb (JPG or PNG). Back-up image only required if you supply an HTML5 banner.
• Looping: Yes
• See Half Page for more information.

I would like them to be quite simple , WYNDALE Your Faulconbridge property experts and another saying WYNDALE your Lawson property experts and WYNDALE your Hazelbrook property experts (3 different versions all up ) and another version MAREE DOLTON your Faulconbridge property expert with logo and her image , i've put a photo of the top banner example and a video of the side banner it has a video in the background that i will get produced if it works

```html
<!DOCTYPE html>
<html lang="en">
<head>
<meta charset="utf-8">
<title>WYNDALE – Banner Ad Set</title>
<link rel="stylesheet" href="https://fonts.googleapis.com/css2?family=Figtree:wght@400;500;800&family=Roboto:wght@400&display=swap">
<style>
  :root {
    --navy: #03104f;
    --navy-panel: #020e4a;
    --white: #ffffff;
    --ink: #111111;
    --paper: #ffffff;
    --photo-light: #efe9e2;
    --photo-mid: #c9bcb0;
    --photo-red: #c8202a;
  }
  * { margin: 0; padding: 0; box-sizing: border-box; }
  html, body {
    width: 1200px;
    height: 1200px;
    overflow: hidden;
    background: var(--paper);
  }
  .sheet {
    position: relative;
    width: 1200px;
    height: 1200px;
    font-family: "Figtree", sans-serif;
    color: var(--white);
  }
  .size-label {
    position: absolute;
    font-family: "Roboto", sans-serif;
    font-size: 26px;
    color: var(--ink);
    line-height: 1;
  }
  .ad {
    position: absolute;
    background: var(--navy);
    overflow: hidden;
  }
  .wordmark {
    position: absolute;
    font-family: "Figtree", sans-serif;
    font-weight: 500;
    letter-spacing: 0.18em;
    line-height: 1;
    white-space: nowrap;
    transform: translate(-50%, -50%);
    color: var(--white);
  }
  .tagline {
    position: absolute;
    font-weight: 400;
    color: var(--white);
    white-space: nowrap;
  }

  /* Skyscraper 160×600 */
  .skyscraper { left: 184px; top: 106px; width: 181px; height: 652px; }
  .skyscraper .tagline {
    left: 0; right: 0; top: 92px;
    text-align: center;
    font-size: 28px;
    line-height: 34px;
  }
  .skyscraper .wordmark { left: 50%; top: 601px; font-size: 22px; }

  /* Mega skyscraper 300×600 */
  .mega { left: 604px; top: 106px; width: 340px; height: 652px; }
  .agent-photo {
    position: absolute;
    left: 0; top: 0; width: 340px; height: 267px;
    background:
      radial-gradient(ellipse 45% 60% at 64% 110%, var(--photo-red) 0 60%, transparent 61%),
      linear-gradient(180deg, var(--photo-light) 0%, var(--photo-light) 58%, var(--photo-mid) 60%, #b3aaa3 100%);
  }
  .agent-name {
    position: absolute;
    left: 0; right: 0; top: 291px;
    text-align: center;
    font-size: 36px;
    font-weight: 800;
    letter-spacing: 0.01em;
    line-height: 1;
  }
  .agent-rule {
    position: absolute;
    left: 82px; top: 357px;
    width: 178px; height: 1.5px;
    background: var(--white);
  }
  .mega .tagline {
    left: 0; right: 0; top: 384px;
    text-align: center;
    font-size: 27px;
    line-height: 34px;
  }
  .mega .wordmark { left: 50%; top: 611px; font-size: 28px; }

  /* Leaderboard 728×90 */
  .leaderboard { left: 184px; top: 846px; width: 840px; height: 97px; }
  .brand-panel {
    position: absolute; left: 0; top: 0; bottom: 0;
    background: var(--navy-panel);
  }
  .leaderboard .brand-panel { width: 269px; }
  .leaderboard .wordmark { left: 134px; top: 49px; font-size: 30px; }
  .divider {
    position: absolute;
    width: 1.5px;
    background: var(--white);
  }
  .leaderboard .divider { left: 285px; top: 14px; height: 70px; }
  .leaderboard .tagline {
    left: 562px; top: 49px;
    transform: translate(-50%, -50%);
    font-size: 25px;
    line-height: 1;
  }

  /* Email alert strip 472×114 */
  .strip { left: 184px; top: 1012px; width: 535px; height: 123px; }
  .strip .brand-panel { width: 233px; }
  .strip .wordmark { left: 114px; top: 62px; font-size: 25px; }
  .strip .divider { left: 242px; top: 19px; height: 86px; }
  .strip .tagline {
    left: 271px; top: 29px;
    font-size: 28px;
    line-height: 34px;
  }
</style>
</head>
<body>
<main class="sheet">

  <span class="size-label" style="left:177px; top:69px;">160×600px</span>
  <section class="ad skyscraper" aria-label="Skyscraper ad">
    <p class="tagline">your<br>Hazelbrook<br>property<br>experts</p>
    <span class="wordmark">WYNDALE</span>
  </section>

  <span class="size-label" style="left:601px; top:69px;">300×600px</span>
  <section class="ad mega" aria-label="Mega skyscraper ad">
    <div class="agent-photo" role="img" aria-label="Portrait photo of agent Maree Dolton in a red jacket, smiling, in a bright kitchen"></div>
    <h2 class="agent-name">MAREE DOLTON</h2>
    <div class="agent-rule"></div>
    <p class="tagline">your Faulconbridge<br>property expert</p>
    <span class="wordmark">WYNDALE</span>
  </section>

  <span class="size-label" style="left:183px; top:810px;">728×90px</span>
  <section class="ad leaderboard" aria-label="Leaderboard ad">
    <div class="brand-panel"></div>
    <span class="wordmark">WYNDALE</span>
    <div class="divider"></div>
    <p class="tagline">Your Faulconbridge property experts</p>
  </section>

  <span class="size-label" style="left:184px; top:976px;">472×114px</span>
  <section class="ad strip" aria-label="Email alert strip ad">
    <div class="brand-panel"></div>
    <span class="wordmark">WYNDALE</span>
    <div class="divider"></div>
    <p class="tagline">your Lawson<br>property experts</p>
  </section>

</main>
</body>
</html>
```